Velmor Glazing

Modern glazing company specializing in commercial fit outs, pool fencing, frameless showers and glass splash backs, im after a very young/modern logo, it doesnt have to be revelent to glazing and a classy "boss like" design for the card. thank you in advanced

im thinking carbon fiber back ground or something along that line with bright orange wording or something maybe, open to suggestions 

Fencing

company name, name, phone and products

```html
<!DOCTYPE html>
<html lang="en">
<head>
<meta charset="utf-8">
<title>Velmor Glazing – Business Card</title>
<link href="https://fonts.googleapis.com/css2?family=Open+Sans:wght@400;600;700&display=swap" rel="stylesheet">
<style>
  :root {
    --stage: #3a3230;
    --card-black: #1c1c1c;
    --card-deep: #141414;
    --band-light: #5a5a5a;
    --band-dark: #262626;
    --orange: #f07a33;
    --text-light: #e8e8e8;
    --text-dark: #1a1a1a;
  }
  * { box-sizing: border-box; margin: 0; padding: 0; }
  html, body { width: 1200px; height: 848px; overflow: hidden; }
  body {
    background: var(--stage);
    font-family: "Open Sans", sans-serif;
    display: flex;
    align-items: center;
    justify-content: center;
    gap: 40px;
  }
  .card {
    position: relative;
    width: 540px;
    height: 310px;
    background: var(--card-black);
    border-radius: 6px;
    overflow: hidden;
    box-shadow: 0 12px 30px rgba(0,0,0,.45);
  }
  .side-band {
    position: absolute;
    top: 0; bottom: 0;
    width: 130px;
    background: linear-gradient(180deg, var(--band-dark) 0%, var(--band-light) 45%, var(--band-dark) 100%);
  }
  .card-front .side-band { left: 220px; }
  .card-back .side-band { left: 40px; }
  .wordmark {
    position: absolute;
    display: flex;
    align-items: center;
    gap: 10px;
    color: var(--orange);
    font-weight: 600;
    font-size: 17px;
    letter-spacing: 4px;
    line-height: 1.15;
    text-transform: uppercase;
  }
  .wordmark .mark-square {
    width: 14px; height: 14px;
    background: var(--orange);
    flex: none;
  }
  .card-front .wordmark { left: 150px; top: 222px; }
  .card-back .wordmark { left: 24px; top: 232px; font-size: 14px; letter-spacing: 3px; }

  .corner-bracket {
    position: absolute;
    top: 40px; right: 0;
    width: 50px; height: 110px;
    background: var(--card-deep);
  }
  .person-name {
    position: absolute;
    left: 210px; top: 30px;
    color: var(--orange);
    font-size: 26px;
    font-weight: 600;
    letter-spacing: 2px;
  }
  .contact-list {
    position: absolute;
    left: 210px; top: 80px;
    list-style: none;
    color: var(--text-light);
    font-size: 13px;
    line-height: 1.6;
  }
  .contact-list li { display: flex; align-items: flex-start; gap: 8px; }
  .contact-list svg { width: 12px; height: 12px; margin-top: 4px; flex: none; fill: #bdbdbd; }
  .contact-list .no-icon { padding-left: 20px; }
  .specialty-title {
    position: absolute;
    left: 195px; top: 196px;
    color: var(--text-light);
    font-size: 14px;
    line-height: 20px;
    letter-spacing: 1px;
    text-transform: uppercase;
  }
  .specialty-bar {
    position: absolute;
    left: 180px; right: 0; bottom: 22px;
    height: 56px;
    background: var(--orange);
    border-radius: 12px 0 0 0;
    padding: 8px 20px;
    display: grid;
    grid-template-columns: 1fr 1fr;
    color: var(--text-dark);
    font-size: 12.5px;
    letter-spacing: .5px;
    text-transform: uppercase;
    line-height: 1.55;
    list-style: none;
  }
</style>
</head>
<body>
  <section class="card card-front" aria-label="Card front">
    <div class="side-band"></div>
    <div class="wordmark"><span class="mark-square"></span><span>Velmor<br>Glazing</span></div>
  </section>

  <section class="card card-back" aria-label="Card back">
    <div class="side-band"></div>
    <div class="wordmark"><span class="mark-square"></span><span>Velmor<br>Glazing</span></div>
    <div class="corner-bracket"></div>

    <h1 class="person-name">DANE MORROW</h1>
    <ul class="contact-list">
      <li><svg viewBox="0 0 12 12"><circle cx="6" cy="4" r="3.5"/><rect x="5.3" y="6" width="1.4" height="6"/></svg>Name Street 123</li>
      <li class="no-icon">State, Town, Country 00000</li>
      <li><svg viewBox="0 0 12 12"><rect x="2.5" y="0" width="7" height="12" rx="1.5"/></svg>0400 555 218</li>
      <li><svg viewBox="0 0 12 12"><path d="M0 2h12v8H0z"/></svg>dmorrow@mail.com</li>
      <li><svg viewBox="0 0 12 12"><path d="M6 0l6 5.5H10V12H2V5.5H0z"/></svg>www.velmorglazing.com</li>
    </ul>

    <p class="specialty-title">Specializing in</p>
    <ul class="specialty-bar">
      <li>Commercial Fit Outs</li>
      <li>Frameless Showers</li>
      <li>Pool Fencing</li>
      <li>Glass Splash Backs</li>
    </ul>
  </section>
</body>
</html>
```